TBNW site redesign

Please redesign a home page with content provided. PSD only - no coding
Can use any images from Vexelmarq.com

Please create a site design that more clearly illustrates the client's services and expertise. We are looking for a high-end design.

Any images used must be generic or of Dallas TX.

Fonts: Any
Colors: Match to logo
Look: Modern - Professional

Target Market(s)

medium-large business owners

Number of Pages Required

1 page

Font styles to use
Serif
Sans Serif

Requirements
Must have
• cohesive professional design
• high end look
• Match to logo

```html
<!DOCTYPE html>
<html lang="en">
<head>
<meta charset="utf-8">
<title>TBNW – Commercial Realty Group</title>
<link href="https://fonts.googleapis.com/css2?family=Playfair+Display:wght@400;700&family=Montserrat:wght@400;500;600;700&display=swap" rel="stylesheet">
<style>
:root{
  --red:#e03c3f;
  --dark:#3c4048;
  --darker:#24262b;
  --ink:#222;
  --muted:#777;
  --line:#e3e3e3;
  --white:#fff;
}
*{margin:0;padding:0;box-sizing:border-box}
html,body{width:1200px;height:4018px;overflow:hidden}
body{font-family:"Montserrat",sans-serif;color:var(--ink);background:var(--white);position:relative}
section,header,footer{position:absolute;left:0;width:1200px}
.eyebrow{font-size:11px;letter-spacing:2px;text-transform:uppercase;color:var(--ink);font-weight:600}
.title{font-family:"Playfair Display",serif;font-size:32px;font-weight:700;color:var(--ink)}
.title em{font-style:normal;color:var(--red)}
.body-text{font-size:13px;line-height:22px;color:var(--muted)}
.btn{display:inline-block;font-size:11px;font-weight:600;letter-spacing:1.5px;text-transform:uppercase;padding:12px 24px}
.btn-red{background:var(--red);color:var(--white)}
.btn-outline-red{border:1px solid var(--red);color:var(--red)}
.btn-outline-white{border:1px solid var(--white);color:var(--white)}
.read-more{font-size:11px;font-weight:600;letter-spacing:1.5px;text-transform:uppercase}
.photo{position:absolute}

/* header */
.site-header{top:0;height:88px;background:var(--white)}
.brand{position:absolute;left:160px;top:28px;display:flex;align-items:center;gap:10px}
.brand-square{width:26px;height:26px;background:var(--red)}
.brand-name{font-family:"Playfair Display",serif;font-weight:700;font-size:26px;color:var(--ink);line-height:1}
.call{position:absolute;right:150px;top:18px;font-family:"Playfair Display",serif;color:var(--red);font-size:20px;display:flex;align-items:center;gap:8px}
.nav{position:absolute;left:490px;top:56px;display:flex;gap:40px;font-size:12px;font-weight:500;letter-spacing:1px}
.nav a{color:var(--ink);text-decoration:none;padding-bottom:8px}
.nav a.active{color:var(--red);border-bottom:2px solid var(--red)}

/* hero */
.hero{top:88px;height:402px}
.hero .photo{inset:0;background:linear-gradient(100deg,#2c3440 0%,#5a6370 40%,#c89860 70%,#e8b466 78%,#4a4a52 100%)}
.hero-copy{position:absolute;left:153px;top:95px;color:var(--white)}
.hero-copy h1{font-family:"Playfair Display",serif;font-size:32px;line-height:38px;font-weight:700}
.hero-copy p{font-size:14px;line-height:22px;margin:18px 0 26px;width:330px}
.slider-dot{position:absolute;right:135px;width:30px;height:30px;border-radius:50%;display:flex;align-items:center;justify-content:center}

/* about */
.about{top:490px;height:403px}
.about-copy{position:absolute;left:153px;top:100px;width:440px}
.about-copy .title{margin:8px 0 18px}
.about-copy .btn{margin-top:22px}
.about .photo{left:600px;top:0;width:600px;height:403px;background:linear-gradient(180deg,#b9cfe0 0%,#8aa0b2 45%,#6d7885 100%)}

/* services */
.services{top:893px;height:533px;background:var(--dark);color:var(--white);text-align:center}
.services .eyebrow{color:var(--white);padding-top:78px}
.services .title{color:var(--white);margin-top:10px;font-size:30px}
.service-grid{position:absolute;left:0;top:210px;width:1200px;display:flex}
.service{width:300px;height:260px;padding:0 36px;border-left:1px solid #54585f}
.service:first-child{border-left:none}
.service svg{height:50px}
.service h3{font-size:14px;font-weight:700;margin:20px 0 14px}
.service p{font-size:12px;line-height:20px;color:#c7c9cd}
.service .read-more{display:block;margin-top:22px}
.service.active h3,.service.active .read-more{color:var(--red)}

/* red band */
.cta-band{top:1426px;height:195px;background:var(--red);color:var(--white)}
.cta-band p{position:absolute;left:153px;top:48px;font-size:21px;line-height:33px;width:620px}
.cta-band .btn{position:absolute;left:840px;top:78px;padding:10px 40px}

/* team */
.team{top:1621px;height:730px}
.team .hero-photo{left:0;top:0;width:600px;height:451px;background:linear-gradient(160deg,#9eb0c4 0%,#5d6c7e 50%,#cfd7df 100%)}
.team-copy{position:absolute;left:665px;top:85px;width:380px}
.team-copy .title{margin:8px 0 22px;font-size:30px}
.team-copy .body-text{font-size:12px;line-height:21px}
.member{position:absolute;top:362px;width:268px}
.member .photo{position:static;height:268px}
.member h4{font-size:14px;font-weight:700;margin-top:26px;padding-bottom:12px;border-bottom:1px solid var(--line)}
.member span{display:block;font-size:10px;color:var(--muted);margin-top:10px}

/* testimonials */
.testimonials{top:2370px;height:320px;text-align:center}
.testimonials .eyebrow{margin-top:30px}
.testimonials .title{font-size:30px;margin-top:6px}
.quote-mark{font-family:"Playfair Display",serif;color:var(--red);font-size:60px;line-height:50px;margin-top:20px}
.testimonials blockquote{font-family:"Playfair Display",serif;font-size:17px;line-height:27px;color:#666;width:820px;margin:0 auto}
.quote-nav{margin-top:24px;font-size:14px;font-weight:600;display:flex;justify-content:center;gap:24px;align-items:center}

/* appointment */
.appointment{top:2739px;height:201px;background:#1c1d21}
.appointment .photo{inset:0;background:linear-gradient(90deg,#2a2b30 0%,#3f4046 50%,#232428 100%)}
.appointment p{position:absolute;left:153px;top:48px;width:600px;color:var(--white);font-size:22px;line-height:34px}
.appointment .btn{position:absolute;left:840px;top:80px;padding:10px 30px}

/* blog */
.blog{top:3000px;height:623px;text-align:center}
.blog .eyebrow{margin-top:30px}
.blog .title{font-size:30px;margin-top:6px}
.blog-arrow{position:absolute;top:28px;width:34px;height:34px;border-radius:50%;display:flex;align-items:center;justify-content:center}
.post{position:absolute;top:110px;width:283px;text-align:left}
.post .photo{position:static;height:160px}
.post time{display:block;color:var(--red);font-size:11px;margin-top:26px}
.post h4{font-size:14px;font-weight:700;line-height:20px;margin:12px 0 12px}
.post p{font-size:12px;line-height:19px;color:var(--muted)}
.post .read-more{display:block;margin-top:28px}
.blog .btn{position:absolute;left:540px;top:494px;padding:10px 34px}

/* footer */
.site-footer{top:3623px;height:395px;background:linear-gradient(135deg,#1d1f23,#2c2e33);color:var(--white)}
.site-footer .eyebrow{color:var(--white);text-align:center;margin-top:78px}
.site-footer .title{color:var(--white);text-align:center;font-size:30px;margin-top:4px}
.foot-col{position:absolute;top:220px}
.foot-col h5{font-size:10px;font-weight:600;letter-spacing:1px;margin-bottom:10px}
.foot-col p{font-size:10px;line-height:15px}
.foot-col .big{font-size:20px;letter-spacing:1px}
.social{display:flex;gap:8px}
.social i{display:block;width:24px;height:24px;border-radius:50%;background:#666}
.social i.on{background:var(--red)}
.copyright{position:absolute;left:153px;top:300px;width:895px;border-top:1px solid #555;padding-top:10px;font-size:10px}
.to-top{position:absolute;right:0;top:6px;width:22px;height:22px;background:#555}
.legal{position:absolute;top:340px;font-size:10px;line-height:14px}
.legal.red{color:var(--red);text-decoration:underline}
</style>
</head>
<body>

<header class="site-header">
  <div class="brand"><span class="brand-square"></span><span class="brand-name">TBNW</span></div>
  <div class="call">Call Today:
    <svg width="20" height="20" viewBox="0 0 24 24"><path d="M6.6 10.8a15 15 0 0 0 6.6 6.6l2.2-2.2a1 1 0 0 1 1-.25 11.4 11.4 0 0 0 3.6.57 1 1 0 0 1 1 1V20a1 1 0 0 1-1 1A17 17 0 0 1 3 4a1 1 0 0 1 1-1h3.5a1 1 0 0 1 1 1c0 1.25.2 2.45.57 3.57a1 1 0 0 1-.25 1z" fill="#e03c3f"/></svg>
    214-555-0142</div>
  <nav class="nav">
    <a class="active">HOME</a><a>ABOUT TBNW</a><a>SERVICES</a><a>BLOG</a><a>MARKET NEWS</a><a>CONTACT US</a>
  </nav>
</header>

<section class="hero">
  <div class="photo" role="img" aria-label="Dallas skyline at sunset"></div>
  <div class="hero-copy">
    <h1>Professional Office<br>and Warehouse Leasing</h1>
    <p>Fast-track your search with tenant reps that only serve you, and specialize in the DFW area.</p>
    <span class="btn btn-red">Contact Us</span>
  </div>
  <div class="slider-dot" style="top:160px;border:1px solid #fff">
    <svg width="12" height="12" viewBox="0 0 12 12"><path d="M8 2 4 6l4 4" stroke="#fff" fill="none" stroke-width="1.5"/></svg></div>
  <div class="slider-dot" style="top:200px;background:#fff">
    <svg width="12" height="12" viewBox="0 0 12 12"><path d="m4 2 4 4-4 4" stroke="#e03c3f" fill="none" stroke-width="1.5"/></svg></div>
</section>

<section class="about">
  <div class="about-copy">
    <div class="eyebrow">Who We Are</div>
    <h2 class="title">About <em>TBNW</em></h2>
    <p class="body-text">There are many variations of passages of Lorem Ipsum available, but the majority have suffered alteration in some form, by injected humour, or randomised words which don't look even slightly believable. If you are going to use a passage of Lorem Ipsum, you need to be sure there isn't anything ...</p>
    <span class="btn btn-outline-red">Discover More</span>
  </div>
  <div class="photo" role="img" aria-label="Aerial view of downtown Dallas"></div>
</section>

<section class="services">
  <div class="eyebrow">Our Services</div>
  <h2 class="title">Why Tenant <em>Representation?</em></h2>
  <div class="service-grid">
    <div class="service">
      <svg viewBox="0 0 60 50" width="60"><path d="M8 20 20 10l10 6 10-6 12 10-22 20z" stroke="#c7c9cd" fill="none" stroke-width="2"/></svg>
      <h3>Relationships</h3>
      <p>Save time by trusting TBNW your team after years find the right location for you. Once we've worked ...</p>
      <span class="read-more">Read More →</span>
    </div>
    <div class="service active">
      <svg viewBox="0 0 60 50" width="60"><rect x="14" y="20" width="32" height="26" rx="3" stroke="#e03c3f" fill="none" stroke-width="2"/><path d="M21 20v-7a9 9 0 0 1 18 0v7" stroke="#e03c3f" fill="none" stroke-width="2"/><circle cx="30" cy="33" r="3" fill="#e03c3f"/></svg>
      <h3>Access to More</h3>
      <p>We have no agreement or personal incentive for specific properties, so we can always show ...</p>
      <span class="read-more">Read More →</span>
    </div>
    <div class="service">
      <svg viewBox="0 0 60 50" width="60"><path d="M14 24h8v22h-8zM22 26l8-16c4 0 5 3 4 7l-1 5h11a4 4 0 0 1 4 5l-3 14a4 4 0 0 1-4 3H22" stroke="#c7c9cd" fill="none" stroke-width="2"/></svg>
      <h3>Free to You</h3>
      <p>You pay us nothing. We get our commission from the property being leased ...</p>
      <span class="read-more">Read More →</span>
    </div>
    <div class="service">
      <svg viewBox="0 0 60 50" width="60"><circle cx="24" cy="28" r="10" stroke="#c7c9cd" fill="none" stroke-width="2"/><circle cx="24" cy="28" r="4" stroke="#c7c9cd" fill="none" stroke-width="2"/><circle cx="42" cy="14" r="7" stroke="#c7c9cd" fill="none" stroke-width="2"/></svg>
      <h3>Customized Service</h3>
      <p>Aside from saving you the time of repeating what you need, we tailor each location ...</p>
      <span class="read-more">Read More →</span>
    </div>
  </div>
</section>

<section class="cta-band">
  <p>If you need to find office or warehouse space in the Dallas Fort Worth area, the team at TBNW has the experience you need.</p>
  <span class="btn btn-outline-white">Space Calculator</span>
</section>

<section class="team">
  <div class="photo hero-photo" role="img" aria-label="Looking up at office towers with a plane overhead"></div>
  <div class="team-copy">
    <div class="eyebrow">Talented People</div>
    <h2 class="title">Meet the <em>Team</em></h2>
    <p class="body-text">At TBNW we believe that you deserve the best professional advice and personal service with your commercial real estate negotiations. By choosing TBNW as your tenant reps in the Dallas/Fort Worth area, you will receive the assistance of accomplished and experienced commercial real estate brokers and salespeople who are licensed by the State Real Estate Commission to practice in Texas since 1982.</p>
  </div>
  <div class="member" style="left:153px">
    <div class="photo" role="img" aria-label="Portrait of the founder" style="background:linear-gradient(180deg,#d9dde2,#8d939b)"></div>
    <h4>Graham T. Tarbell</h4><span>Founder and President</span>
  </div>
  <div class="member" style="left:466px">
    <div class="photo" role="img" aria-label="Portrait of the senior director" style="background:linear-gradient(180deg,#9bb4c8,#4d5a66)"></div>
    <h4>Mark Ellison-Reyes</h4><span>Senior Director, Commercial Property Specialist</span>
  </div>
  <div class="member" style="left:780px">
    <div class="photo" role="img" aria-label="Portrait of the associate" style="background:linear-gradient(180deg,#c2c8ce,#5b544f)"></div>
    <h4>Nathan Cole Whitford</h4><span>Jr., Associate, Tenant Rep Specialist</span>
  </div>
</section>

<section class="testimonials">
  <div class="eyebrow">Testimonials</div>
  <h2 class="title">What Our <em>Clients Say</em></h2>
  <div class="quote-mark">“</div>
  <blockquote>"The real estate team at TBNW has decades of experience in Commercial. One advantage of TBNW is they know all the properties that are about to become available, BEFORE they are available. They have the inside track on properties and they watch your back at the negotiating table..."</blockquote>
  <div class="quote-nav"><span>←</span><span>— Daniel Avery Marsh</span><span>→</span></div>
</section>

<section class="appointment">
  <div class="photo" role="img" aria-label="Dark steel lattice ceiling"></div>
  <p>Whether your lease is expiring soon, or you're just starting your search, TBNW can help you find the perfect space.</p>
  <span class="btn btn-red">Make an Appointment</span>
</section>

<section class="blog">
  <div class="blog-arrow" style="left:278px;border:1px solid #e03c3f"><svg width="12" height="12" viewBox="0 0 12 12"><path d="M8 2 4 6l4 4" stroke="#e03c3f" fill="none" stroke-width="1.5"/></svg></div>
  <div class="blog-arrow" style="left:888px;background:#e03c3f"><svg width="12" height="12" viewBox="0 0 12 12"><path d="m4 2 4 4-4 4" stroke="#fff" fill="none" stroke-width="1.5"/></svg></div>
  <div class="eyebrow">Latest Blog</div>
  <h2 class="title">Recent <em>Articles</em></h2>
  <article class="post" style="left:153px">
    <div class="photo" role="img" aria-label="Empty modern office interior" style="background:linear-gradient(180deg,#8fa0a8,#d5dadd)"></div>
    <time>17 FEB 2018</time><h4>There are many variations of passages of Lorem</h4>
    <p>There are many variations of passages of Lorem Ipsum available, but the majority have suffered alteration in some form ...</p>
    <span class="read-more">Read More →</span>
  </article>
  <article class="post" style="left:459px">
    <div class="photo" role="img" aria-label="Glass office towers against blue sky" style="background:linear-gradient(180deg,#6f9acb,#2f4f79)"></div>
    <time>20 MARCH 2018</time><h4>There are many variations of passages of Lorem</h4>
    <p>There are many variations of passages of Lorem Ipsum available, but the majority have suffered alteration in some form ...</p>
    <span class="read-more" style="color:var(--red)">Read More →</span>
  </article>
  <article class="post" style="left:765px">
    <div class="photo" role="img" aria-label="Blue glass skyscraper facades" style="background:linear-gradient(180deg,#4f86c2,#1f3f70)"></div>
    <time>05 MAY 2018</time><h4>There are many variations of passages of Lorem</h4>
    <p>There are many variations of passages of Lorem Ipsum available, but the majority have suffered alteration in some form ...</p>
    <span class="read-more">Read More →</span>
  </article>
  <span class="btn btn-outline-red">View All</span>
</section>

<footer class="site-footer">
  <div class="eyebrow">Contact Us</div>
  <h2 class="title">Get in <em>Touch</em></h2>
  <div class="foot-col" style="left:153px"><h5>ADDRESS:</h5><p>410 Harwell Avenue, Suite 600<br>Dallas, TX 75201</p></div>
  <div class="foot-col" style="left:459px"><h5>TEL:</h5><p class="big">214-555-0142</p></div>
  <div class="foot-col" style="left:688px"><h5>FAX:</h5><p class="big">214-555-0187</p></div>
  <div class="foot-col" style="left:895px"><h5>GET SOCIAL:</h5><div class="social"><i></i><i class="on"></i><i></i><i></i></div></div>
  <div class="copyright">© 2018 TBNW. All Right Reserved.<span class="to-top"></span></div>
  <p class="legal" style="left:153px">State Real Estate Commission<br>Mandated Disclosure Notices – click links<br>below to view pages</p>
  <p class="legal red" style="left:459px">State Real Estate<br>Commission Information About<br>Brokerage Services</p>
  <p class="legal" style="left:688px;text-decoration:underline">State Real Estate<br>Commission Consumer Protection<br>Notice</p>
</footer>

</body>
</html>
```